Breezy Burro Menu Design for new restaurant

Need a menu design for new restaurant- Fast Casual Taqueria. I have the files for our logo and menu already completed. Let me know what type of file your require and I can send it with regard to my logo. I want it to be easy to read but on a half page rack size type card, front and back. Simple and to the point but important to include the items listed with ingredients. Feel free to use icons for different categories.

Target Market(s)

Any one who loves tacos and margaritas...fun...festive...casual...

Font styles to use
Other font styles liked:
• lobster 1.3 and farmer round

Colors
3276b5
ec1f27
ffffff
85cae6
9bcb3c
fbed22

Requirements
Must have
• Designed for a half page, front and back (4.25 x 11). NO full size page menu. Easy to read. Not complicated. Use our logo. I need to be able to modify the menu from my end with out any special software.
Nice to have
• Fun~Festive~ color. Stick with our logo theme using our font lobster 1.3 and farmer round.
Should not have
• Full page format. Do not want stock food phots. Just graphics or icons.

```html
<!DOCTYPE html>
<html lang="en">
<head>
<meta charset="utf-8">
<title>Breezy Burro Menu</title>
<link href="https://fonts.googleapis.com/css2?family=Oswald:wght@300;400&family=Cinzel:wght@700&display=swap" rel="stylesheet">
<style>
:root{
  --navy:#2d3e50;
  --aqua:#bfe5e5;
  --band:#8fb5bd;
  --red:#ec1f27;
  --paper:#ffffff;
  --art:rgba(45,62,80,.55);
}
*{margin:0;padding:0;box-sizing:border-box}
html,body{width:1200px;height:1092px;overflow:hidden;background:var(--paper)}
body{position:relative;font-family:'Oswald',sans-serif;color:var(--navy);font-variant:small-caps}
.panel{position:absolute;top:0;height:1090px;background:var(--aqua)}
.panel--front{left:273px;width:446px}
.panel--back{left:753px;width:447px}
.abs{position:absolute}
.logo-plate{left:330px;top:15px;width:333px;height:177px;background:var(--navy);border-radius:18px}
.screw{position:absolute;width:15px;height:15px;border-radius:50%;background:var(--aqua)}
.logo-name{left:330px;top:15px;width:333px;height:177px;display:flex;align-items:center;justify-content:center;font-family:'Oswald',sans-serif;font-weight:400;font-variant:normal;font-size:38px;color:var(--red)}
.banner{background:var(--navy);color:var(--aqua);display:flex;flex-direction:column;align-items:center;justify-content:center;border-top:6px solid var(--band);border-bottom:6px solid var(--band);font-weight:400;line-height:1}
.banner__title{font-size:17px}
.banner__sub{font-size:8px;margin-top:3px}
.item__name{font-size:16px;font-weight:300;line-height:17px;white-space:nowrap}
.item__desc{font-size:10px;font-weight:300;line-height:17.8px;white-space:nowrap}
.item--right{text-align:right}
.art{background:var(--art);border-radius:6px}
.bev{right:60px;text-align:right;font-family:'Cinzel',serif;font-variant:normal;line-height:1;white-space:nowrap}
.bev__name{font-size:13px}
.bev__size{font-size:8px;font-weight:700}
.blank{display:inline-block;border-bottom:1px solid var(--navy);height:6px;vertical-align:baseline}
</style>
</head>
<body>
<div class="panel panel--front"></div>
<div class="panel panel--back"></div>

<!-- Front: name plate -->
<div class="abs logo-plate">
  <span class="screw" style="left:8px;top:13px"></span>
  <span class="screw" style="right:16px;top:13px"></span>
  <span class="screw" style="left:8px;bottom:13px"></span>
  <span class="screw" style="right:16px;bottom:13px"></span>
</div>
<div class="abs logo-name">Breezy Burro</div>

<div class="abs banner" style="left:329px;top:213px;width:242px;height:56px;align-items:flex-start;padding-left:8px">
  <span class="banner__title">Let’s get this party started…</span>
</div>

<div class="abs item" style="left:330px;top:280px">
  <div class="item__name">Mexican Poke</div>
  <div class="item__desc">Fresh Ahi Tuna blended w/ spices &amp; ponzu on a bed of colored cabbage</div>
</div>
<div class="abs item" style="left:330px;top:333px">
  <div class="item__name">Mermaid Tails</div>
  <div class="item__desc">Shrimp Tempura beached on coconut slaw w/ sweet heat glaze, rice<br>pearls, fresh cilantro</div>
</div>
<div class="abs item" style="left:330px;top:403px">
  <div class="item__name">FIESTA NACHOS</div>
  <div class="item__desc">Crunchy tortilla chips layered w/ queso fresco, pickled vegetables,<br>black beans tomatillo salsa, dry chile salsa &amp;cilantro. As flavorful<br>as it is colorful! *add any protein for upcharge</div>
</div>
<div class="abs item" style="left:330px;top:492px">
  <div class="item__name">CHORIZO &amp; QUESO</div>
  <div class="item__desc">Melted queso fresco w/ Chorizo crumbles, caramelized onions, cilantro</div>
</div>
<div class="abs item" style="left:330px;top:545px">
  <div class="item__name">ELOTE</div>
  <div class="item__desc">Roasted corn sliced from the cob, chopped onions and poblano peppers<br>w/ cotija cheese, smoky homemade morita mayo &amp; Chulita</div>
</div>
<div class="abs item" style="left:330px;top:615px">
  <div class="item__name">GUACAMOLE &amp; CHIPS</div>
  <div class="item__desc">Smooth blend of Haas avocados, jalapeño, red onions</div>
</div>
<div class="abs item" style="left:330px;top:668px">
  <div class="item__name">CHIPS AND SALSA</div>
  <div class="item__desc">Tortilla chips w/ choice of traditional rojo salsa or tomatillo verde</div>
</div>
<div class="abs item" style="left:330px;top:721px">
  <div class="item__name">QUESO AND CHIPS</div>
  <div class="item__desc">Melted queso fresco &amp; crunchy tortilla chips</div>
</div>
<div class="abs item" style="left:330px;top:774px">
  <div class="item__name">RICE &amp; BLACK BEANS</div>
  <div class="item__desc">Traditional Mexican arroz verde &amp; black beans seasoned w/ epazote</div>
</div>

<div class="abs art" role="img" aria-label="Line drawing of a wrapped burrito" style="left:598px;top:238px;width:98px;height:196px"></div>
<div class="abs art" role="img" aria-label="Sombrero icon" style="left:604px;top:652px;width:93px;height:59px"></div>
<div class="abs art" role="img" aria-label="Hand lettered word Yummy" style="left:541px;top:717px;width:173px;height:113px"></div>
<div class="abs art" role="img" aria-label="Steaming bowl icon" style="left:306px;top:893px;width:158px;height:130px"></div>

<div class="abs banner" style="left:510px;top:848px;width:152px;height:59px">
  <span class="banner__title" style="font-size:19px">BOWL ME OVER!</span>
  <span class="banner__sub">MAKE ANY BREEZY TACO INTO A BOWL</span>
</div>
<div class="abs item item--right" style="right:540px;top:928px">
  <div class="item__name">Ensalada</div>
  <div class="item__desc" style="line-height:14px">Chopped field greens, black beans, elote, avocado<br>smash, fresh cilantro &amp; queso fresco</div>
</div>
<div class="abs item item--right" style="right:537px;top:984px">
  <div class="item__name">Rice &amp; Beans</div>
  <div class="item__desc" style="line-height:14px">Traditional Mexican arroz verde, seasoned black<br>beans &amp; queso fresco</div>
</div>

<!-- Back: tacos -->
<div class="abs banner" style="left:809px;top:19px;width:107px;height:58px">
  <span class="banner__title" style="font-size:19px">Tacos</span>
</div>
<div class="abs item" style="left:812px;top:83px">
  <div class="item__desc">*All tacos finished Breezy Style with fresh cilantro, side of dry chile<br>salsa &amp; lime wedges</div>
</div>
<div class="abs item" style="left:812px;top:113px"><div class="item__name">Korean</div><div class="item__desc">braised short ribs, caramelized onions, cucumber salad, Gochujang sauce</div></div>
<div class="abs item" style="left:812px;top:148px"><div class="item__name">BARBACOA</div><div class="item__desc">spiced Angus beef, cool creama, white diced onion, tomatillo-avocado salsa</div></div>
<div class="abs item" style="left:812px;top:183px"><div class="item__name">Al Pastor</div><div class="item__desc">spit-grilled Heritage Pork, diced white onion, charred pineapple<br>queso fresco</div></div>
<div class="abs item" style="left:812px;top:236px"><div class="item__name">Carnitas</div><div class="item__desc">slow simmered Heritage Pork, avocado smash, pickled red onion, blistered<br>shishito peppers</div></div>
<div class="abs item" style="left:812px;top:289px"><div class="item__name">Alabama Slamma</div><div class="item__desc">pulled smoked chicken, Alabama White Sauce, pickled cabbage, fried onions,<br>bacon blanket</div></div>
<div class="abs item" style="left:812px;top:342px"><div class="item__name">Chick Next Door</div><div class="item__desc">grilled chicken breast, elote, avocado smash, queso fresco, salsa verde</div></div>
<div class="abs item" style="left:812px;top:378px"><div class="item__name">Yinzer</div><div class="item__desc">grilled flat iron steak w/peppers &amp; onions, melted queso fresco, house<br>jalapeño salsa, chicharrónes</div></div>
<div class="abs item" style="left:812px;top:431px"><div class="item__name">Beach Bum</div><div class="item__desc">maple fire roasted sweet potato, seasoned black beans, tropical slaw<br>toasted coconut</div></div>
<div class="abs item" style="left:812px;top:484px"><div class="item__name">Island Time</div><div class="item__desc">battered avocado, sweet teriyaki glaze, charred pineapple, pickled<br>red onion, queso fresco</div></div>
<div class="abs item" style="left:812px;top:537px"><div class="item__name">Tropical Shrimp</div><div class="item__desc">Shrimp Tempura, avocado smash, tropical slaw, sweet heat creama,<br>toasted coconut</div></div>
<div class="abs item" style="left:812px;top:590px"><div class="item__name">Cabo Fish</div><div class="item__desc">beer battered Cod, pickled cabbage, spicy escabeche and smoky homemade<br>morita mayo<br>*only GF if on corn tortilla, filling is GF however…try in a rice or ensalada bowl!</div></div>

<div class="abs art" role="img" aria-label="Hand lettered badge reading Best Cuisine" style="left:1089px;top:80px;width:74px;height:96px"></div>
<div class="abs art" role="img" aria-label="Taco icon with Good Idea Always lettering" style="left:1047px;top:452px;width:134px;height:134px"></div>
<div class="abs art" role="img" aria-label="Frothy beer glass icon" style="left:776px;top:815px;width:140px;height:211px"></div>

<!-- Back: beverages -->
<div class="abs banner" style="left:1006px;top:680px;width:135px;height:56px">
  <span class="banner__title" style="font-size:19px">BEVERAGES</span>
</div>
<div class="abs bev bev__name" style="top:741px">Tea</div>
<div class="abs bev bev__size" style="top:762px">20 oz<span class="blank" style="width:50px"></span></div>
<div class="abs bev bev__name" style="top:771px">Soda Fountain</div>
<div class="abs bev bev__size" style="top:791px">20 oz<span class="blank" style="width:50px"></span></div>
<div class="abs bev bev__name" style="top:802px">Bottle Soda</div>
<div class="abs bev bev__size" style="top:822px">see selection</div>
<div class="abs bev bev__name" style="top:831px">Draft Beer</div>
<div class="abs bev bev__size" style="top:852px">16 oz<span class="blank" style="width:12px"></span> Pitcher<span class="blank" style="width:20px"></span></div>
<div class="abs bev bev__size" style="top:867px">Bottle Beer Import / Domestic–see selection</div>
<div class="abs bev bev__name" style="top:877px">FZ Margarita</div>
<div class="abs bev bev__size" style="top:897px">16 oz<span class="blank" style="width:48px"></span> Pitcher<span class="blank" style="width:50px"></span></div>
<div class="abs bev bev__name" style="top:906px">Tap Margarita 1</div>
<div class="abs bev bev__size" style="top:927px">6 oz<span class="blank" style="width:52px"></span> Pitcher<span class="blank" style="width:48px"></span></div>
<div class="abs bev bev__name" style="top:937px">Sangria</div>
<div class="abs bev bev__size" style="top:957px">16 oz<span class="blank" style="width:30px"></span> Pitcher<span class="blank" style="width:42px"></span></div>
<div class="abs bev bev__name" style="top:967px">Tequila Single Shot</div>
<div class="abs bev bev__size" style="top:988px">Cheap<span class="blank" style="width:4px"></span> Standard<span class="blank" style="width:42px"></span> Premium<span class="blank" style="width:42px"></span></div>
<div class="abs bev bev__name" style="top:997px">Tequila Double Shot</div>
<div class="abs bev bev__size" style="top:1017px">Cheap&nbsp;&nbsp; Standard<span class="blank" style="width:42px"></span> Premium<span class="blank" style="width:42px"></span></div>
</body>
</html>
```